The Larkspur Whiskey & Coffee - Bar Menu

The Larkspur is a speakeasy style coffee and whiskey bar. Upscale with design elements tying in both prohibition era elegance and modern touches.

Black and Gold are our colors. (see logo)

We would need a 8 page menu- front and back. 4.24 in x 11 in for each page. The pages would be:

Intro page
Food/Dessert
Cocktails x 2 pages
Wine- Glass Pour
Wine- Bottle only
Beer
Non-Alcoholic Beverages

Attached is the menu cocktails and food/non alcoholic.

We need an editable format as this menu would be constantly changing.

UPDATE: The owner would potentially like to see the use of the original floor plans incorporated into the menu design. I have uploaded those to this brief.

UPDATE: I have added some photos that show the style the owner would like the writing to be displayed.

Requirements
Should not have
• No pictures of wine or beer or other images. Clipart could be fine, but we want to showcase class and an upscale vibe.

```html
<!DOCTYPE html>
<html lang="en">
<head>
<meta charset="utf-8">
<title>The Larkspur Whiskey &amp; Coffee – Menu</title>
<link href="https://fonts.googleapis.com/css2?family=Barlow+Condensed:wght@500;600&family=Barlow:wght@300&display=swap" rel="stylesheet">
<style>
  :root {
    --gold: #d6b25e;
    --gold-line: #a88a45;
    --gold-wash: rgba(214,178,94,.14);
    --ink: #070707;
    --cream: #f1efe9;
    --page-bg: #ffffff;
  }
  html, body {
    margin: 0;
    width: 1200px;
    height: 777px;
    overflow: hidden;
    background: var(--page-bg);
  }
  .sheet {
    position: absolute;
    left: 0;
    top: 0;
    width: 2380px;
    height: 1540px;
    transform: scale(0.5042);
    transform-origin: 0 0;
    font-family: "Barlow", sans-serif;
  }
  .spread {
    position: absolute;
    width: 1155px;
    height: 1498px;
    overflow: hidden;
    background: var(--ink);
  }
  .spread--cover { left: 19px; top: 20px; }
  .spread--inside { left: 1205px; top: 22px; }

  .backdrop { position: absolute; inset: 0; }
  .spread--cover .backdrop {
    background:
      radial-gradient(ellipse 180px 700px at 180px 500px, rgba(80,80,80,.35), transparent 70%),
      radial-gradient(ellipse 180px 700px at 780px 450px, rgba(80,80,80,.3), transparent 70%),
      linear-gradient(180deg, #262626 0%, #0e0e0e 45%, #020202 100%);
  }
  .spread--inside .backdrop {
    background:
      radial-gradient(ellipse 600px 260px at 850px 130px, rgba(120,120,120,.35), transparent 75%),
      radial-gradient(ellipse 500px 400px at 250px 750px, rgba(70,70,70,.35), transparent 75%),
      radial-gradient(ellipse 400px 500px at 1000px 900px, rgba(70,70,70,.3), transparent 75%),
      linear-gradient(180deg, #2a2a2a 0%, #141414 40%, #050505 100%);
  }
  .fold {
    position: absolute;
    left: 577px;
    top: 0;
    width: 1px;
    height: 100%;
    background: var(--gold-line);
    opacity: .7;
  }

  .wordmark {
    position: absolute;
    margin: 0;
    font-family: "Barlow Condensed", sans-serif;
    font-weight: 600;
    color: var(--gold);
    text-align: center;
    text-transform: uppercase;
    line-height: 1;
  }
  .wordmark span { display: block; }
  .wordmark--cover { left: 598px; width: 540px; top: 765px; }
  .wordmark--cover .wordmark__name { font-size: 76px; letter-spacing: 6px; }
  .wordmark--cover .wordmark__trade { font-size: 30px; letter-spacing: 6px; margin-top: 8px; }

  .pennant { position: absolute; left: 209px; top: 0; width: 166px; height: 232px; }
  .wordmark--pennant { left: 209px; width: 166px; top: 128px; }
  .wordmark--pennant .wordmark__name { font-size: 26px; letter-spacing: 2px; }
  .wordmark--pennant .wordmark__trade { font-size: 12px; letter-spacing: 1.5px; margin-top: 3px; }

  .divider { position: absolute; left: 120px; width: 340px; height: 10px; }
  .divider::before, .divider::after {
    content: ""; position: absolute; top: 4px; width: 150px; height: 1px; background: var(--gold-line);
  }
  .divider::before { left: 0; }
  .divider::after { right: 0; }
  .divider__dot {
    position: absolute; left: 167px; top: 2px; width: 5px; height: 5px; border-radius: 50%; background: var(--gold);
  }
  .divider--top { top: 478px; }
  .divider--bottom { top: 929px; }

  .house-notes {
    position: absolute;
    left: 105px;
    width: 375px;
    top: 575px;
    margin: 0;
    padding: 0;
    list-style: none;
    color: var(--gold);
    font-size: 17px;
    line-height: 23px;
    text-align: center;
    letter-spacing: .5px;
  }
  .house-notes li { margin-bottom: 33px; }
  .house-notes li::before { content: "• "; }

  .building-sketch {
    position: absolute;
    left: 110px;
    top: 1178px;
    width: 345px;
    height: 238px;
    background: linear-gradient(180deg, transparent 0%, var(--gold-wash) 100%);
  }
  .baseline {
    position: absolute; left: 33px; top: 1418px; width: 507px; height: 1px; background: var(--gold-line);
  }

  .menu-column { position: absolute; left: 625px; width: 476px; }
  .menu-column--food { top: 270px; }
  .menu-column--desserts { top: 876px; }
  .section-title {
    margin: 0;
    border-top: 1px solid var(--gold-line);
    border-bottom: 1px solid var(--gold-line);
    padding: 6px 12px 4px;
    font-family: "Barlow Condensed", sans-serif;
    font-weight: 600;
    font-size: 42px;
    line-height: 42px;
    letter-spacing: 3px;
    color: var(--gold);
    text-transform: uppercase;
  }
  .dish-list { list-style: none; margin: 0; padding: 0 0 0 10px; }
  .dish {
    padding: 14px 0 8px;
    border-bottom: 1px dashed rgba(214,178,94,.35);
  }
  .dish:last-child { border-bottom: none; }
  .dish__head { display: flex; justify-content: space-between; padding-right: 20px; }
  .dish__name, .dish__price {
    font-family: "Barlow Condensed", sans-serif;
    font-weight: 500;
    font-size: 27px;
    line-height: 26px;
    letter-spacing: -.3px;
    color: var(--cream);
    text-transform: uppercase;
  }
  .dish__desc {
    margin: 2px 0 0;
    font-size: 15px;
    line-height: 20px;
    color: var(--gold);
    letter-spacing: .2px;
    white-space: nowrap;
  }
</style>
</head>
<body>
<main class="sheet">

  <section class="spread spread--cover">
    <div class="backdrop" role="img" aria-label="Dark, softly blurred photograph of the bar's interior"></div>
    <div class="fold"></div>
    <h1 class="wordmark wordmark--cover">
      <span class="wordmark__name">The Larkspur</span>
      <span class="wordmark__trade">Whiskey &amp; Coffee</span>
    </h1>
  </section>

  <section class="spread spread--inside">
    <div class="backdrop" role="img" aria-label="Dark, blurred photograph of the bar room and seating"></div>
    <div class="fold"></div>

    <svg class="pennant" viewBox="0 0 166 232" aria-hidden="true">
      <polygon points="0,0 166,0 166,52 160,58 160,180 83,210 6,180 6,58 0,52" fill="#0a0a0a"/>
    </svg>
    <div class="wordmark wordmark--pennant">
      <span class="wordmark__name">The Larkspur</span>
      <span class="wordmark__trade">Whiskey &amp; Coffee</span>
    </div>

    <div class="divider divider--top"><span class="divider__dot"></span></div>
    <ul class="house-notes">
      <li>The Larkspur Whiskey &amp; Coffee Reserves the right to change menus selections, and/or the prices that accompany those items, as they appear on the menus at the restaurant.</li>
      <li>Only one promotion/special/discount/kickback may be used at one time, per table or check.</li>
      <li>20% service charged added onto bills of parties of 6 or more.</li>
    </ul>
    <div class="divider divider--bottom"><span class="divider__dot"></span></div>

    <div class="building-sketch" role="img" aria-label="Gold line sketch of the historic bar building"></div>
    <div class="baseline"></div>

    <div class="menu-column menu-column--food">
      <h2 class="section-title">Food</h2>
      <ul class="dish-list">
        <li class="dish"><div class="dish__head"><span class="dish__name">Bone Marrow</span><span class="dish__price">$20</span></div><p class="dish__desc">Bone marrow roasted with sea salt and served with warm tortillas.</p></li>
        <li class="dish"><div class="dish__head"><span class="dish__name">Charcuterie Board</span><span class="dish__price">$25</span></div><p class="dish__desc">Assorted artisan meats and cheeses, nuts, and fruits.</p></li>
        <li class="dish"><div class="dish__head"><span class="dish__name">Hummus, Veggie &amp; Pita</span><span class="dish__price">$16</span></div><p class="dish__desc">Assorted vegetables with warm pita and roasted garlic hummus.</p></li>
        <li class="dish"><div class="dish__head"><span class="dish__name">Lamb Chops</span><span class="dish__price">$18</span></div><p class="dish__desc">Lamb chops broiled with rosemary.</p></li>
        <li class="dish"><div class="dish__head"><span class="dish__name">Tuna Tower</span><span class="dish__price">$17</span></div><p class="dish__desc">Fresh tuna served with white rice, avocado and spice.</p></li>
        <li class="dish"><div class="dish__head"><span class="dish__name">Lettuce Wrap- Walnut Shrimp</span><span class="dish__price">$13</span></div><p class="dish__desc">Honey walnut aioli coated shrimp and lettuce cups with a candied walnut.</p></li>
      </ul>
    </div>

    <div class="menu-column menu-column--desserts">
      <h2 class="section-title">Desserts</h2>
      <ul class="dish-list">
        <li class="dish"><div class="dish__head"><span class="dish__name">Tart</span></div><p class="dish__desc">Your choice of apple or berry with vanilla ice cream.</p></li>
        <li class="dish"><div class="dish__head"><span class="dish__name">Cheesecake</span></div><p class="dish__desc">Chocolate or strawberry drizzle.</p></li>
      </ul>
    </div>
  </section>

</main>
</body>
</html>
```